TalkWell needs a Letterhead

We need a letterhead for our company "TalkWell Consultants". Logo is attached. The company color is Turquoise. Icons for website, scan logo for website, icons for address, e-mail and phone appreciated rather than just words.

```html
<!DOCTYPE html>
<html lang="en">
<head>
<meta charset="utf-8">
<title>TalkWell Consultants – Letterhead</title>
<link href="https://fonts.googleapis.com/css2?family=Mulish:wght@400;700&display=swap" rel="stylesheet">
<style>
  :root {
    --backdrop: #e4e5e7;
    --paper: #ffffff;
    --brand-blue: #2a7bbf;
    --brand-green: #7ab33d;
    --text: #555a60;
    --text-strong: #3a3d41;
    --text-muted: #8a8e93;
    --faint: #f1f2f3;
  }
  * { box-sizing: border-box; margin: 0; padding: 0; }
  html, body { width: 1200px; height: 968px; overflow: hidden; }
  body {
    background: var(--backdrop);
    font-family: "Mulish", sans-serif;
    color: var(--text);
    display: flex;
    align-items: center;
    justify-content: center;
  }
  .letterhead {
    position: relative;
    width: 640px;
    height: 906px;
    background: var(--paper);
    box-shadow: 0 2px 10px rgba(0,0,0,.12);
  }
  .brand {
    position: absolute;
    left: 56px; top: 48px;
    display: flex; align-items: center; gap: 10px;
  }
  .brand-square { width: 26px; height: 26px; background: var(--brand-blue); }
  .brand-name { font-size: 20px; font-weight: 400; color: var(--brand-blue); letter-spacing: .2px; }

  .letter-body {
    position: absolute;
    left: 56px; top: 160px; width: 520px;
    font-size: 11px; line-height: 1.5; font-style: italic;
  }
  .salutation { font-style: normal; font-weight: 700; font-size: 13px; color: var(--text-strong); margin-bottom: 14px; }
  .letter-body p { margin-bottom: 14px; text-align: justify; }

  .sign-off {
    position: absolute;
    right: 64px; top: 640px;
    text-align: right;
  }
  .signature { width: 110px; height: 34px; background: linear-gradient(90deg, #d9dbde, #c6c9cd); margin-left: auto; margin-bottom: 6px; }
  .closing { font-size: 11px; font-style: italic; }
  .signatory { font-size: 15px; font-weight: 700; color: var(--text-strong); margin-top: 2px; }

  .contact {
    position: absolute;
    left: 56px; top: 640px;
    font-size: 9px; color: var(--text-muted);
  }
  .rule { height: 4px; width: 80px; border-radius: 2px; margin-bottom: 10px; }
  .rule-blue { background: var(--brand-blue); }
  .rule-green { background: var(--brand-green); }
  .contact-list { list-style: none; }
  .contact-list li { display: flex; align-items: center; gap: 6px; line-height: 15px; }
  .contact-list svg { width: 11px; height: 11px; flex: none; }

  .address {
    position: absolute;
    right: 64px; top: 800px; width: 170px;
    font-size: 10px; line-height: 1.45; color: var(--text-strong);
  }
  .address .reg { font-size: 8px; color: var(--text-muted); margin-top: 4px; }

  .corner-mark {
    position: absolute;
    left: 160px; top: 770px;
    width: 70px; height: 70px; background: var(--faint);
  }
</style>
</head>
<body>
  <main class="letterhead">
    <header class="brand">
      <span class="brand-square"></span>
      <span class="brand-name">TalkWell Consultants</span>
    </header>

    <section class="letter-body">
      <h2 class="salutation">Dear sir / madame,</h2>
      <p>Lorem ipsum dolor sit amet, consectetur adipisicing elit, sed do eiusmod tempor incididunt ut labore et dolore magna aliqua. Ut enim ad minim veniam, quis nostrud exercitation ullamco laboris nisi ut aliquip ex ea commodo consequat. Duis aute irure dolor in reprehenderit in voluptate velit esse cillum dolore eu fugiat nulla pariatur. Excepteur sint occaecat cupidatat non proident, sunt in culpa qui officia deserunt mollit anim id est laborum. Lorem ipsum dolor sit amet, consectetur adipisicing elit, sed do eiusmod tempor incididunt ut labore et dolore magna aliqua. Ut enim ad minim veniam, quis nostrud exercitation ullamco laboris nisi ut aliquip ex ea commodo consequat. Duis aute irure dolor in reprehenderit in voluptate velit esse cillum dolore eu fugiat nulla pariatur. Excepteur sint occaecat cupidatat non proident, sunt in culpa qui officia deserunt mollit anim id est laborum.</p>
      <p>Lorem ipsum dolor sit amet, consectetur adipisicing elit, sed do eiusmod tempor incididunt ut labore et dolore magna aliqua. Ut enim ad minim veniam, quis nostrud exercitation ullamco laboris nisi ut aliquip ex ea commodo consequat. Duis aute irure dolor in reprehenderit in voluptate velit esse cillum dolore eu fugiat nulla pariatur. Excepteur sint occaecat cupidatat non proident, sunt in culpa qui officia deserunt mollit anim id est laborum.</p>
      <p>Lorem ipsum dolor sit amet, consectetur adipisicing elit, sed do eiusmod tempor incididunt ut labore et dolore magna aliqua. Ut enim ad minim veniam, quis nostrud exercitation ullamco laboris nisi ut aliquip ex ea commodo consequat. Duis aute irure dolor in reprehenderit in voluptate velit esse cillum dolore eu fugiat nulla pariatur. Excepteur sint occaecat cupidatat non proident, sunt in culpa qui officia deserunt mollit anim id est laborum.</p>
      <p>Lorem ipsum dolor sit amet, consectetur adipisicing elit, sed do eiusmod tempor incididunt ut labore et dolore magna aliqua. Ut enim ad minim veniam, quis nostrud exercitation ullamco laboris nisi ut aliquip ex ea commodo consequat. Duis aute irure dolor in reprehenderit in voluptate velit esse cillum dolore eu fugiat nulla pariatur. Excepteur sint occaecat cupidatat non proident, sunt in culpa qui officia deserunt mollit anim id est laborum.</p>
    </section>

    <aside class="contact">
      <div class="rule rule-blue"></div>
      <ul class="contact-list">
        <li>
          <svg viewBox="0 0 12 12"><circle cx="6" cy="6" r="5.5" fill="none" stroke="#2a7bbf"/><path d="M4 3.2l1 1.2-.6.7c.4.9 1 1.5 1.9 1.9l.7-.6 1.2 1-.6 1C5.6 8.2 3.8 6.4 3.6 4z" fill="#2a7bbf"/></svg>
          (03) 5550 1234
        </li>
        <li>
          <svg viewBox="0 0 12 12"><circle cx="6" cy="6" r="5.5" fill="none" stroke="#2a7bbf"/><rect x="3.5" y="4.5" width="5" height="3.5" fill="#2a7bbf"/><rect x="4.5" y="3" width="3" height="1.5" fill="#2a7bbf"/></svg>
          (03) 5550 1235
        </li>
        <li>
          <svg viewBox="0 0 12 12"><circle cx="6" cy="6" r="5.5" fill="none" stroke="#7ab33d"/><rect x="3.2" y="4" width="5.6" height="4" fill="none" stroke="#7ab33d" stroke-width=".8"/><path d="M3.2 4L6 6.3 8.8 4" fill="none" stroke="#7ab33d" stroke-width=".8"/></svg>
          info@talkwell.example
        </li>
        <li>
          <svg viewBox="0 0 12 12"><circle cx="6" cy="6" r="5.5" fill="none" stroke="#7ab33d"/><circle cx="6" cy="6" r="2.8" fill="none" stroke="#7ab33d" stroke-width=".8"/><path d="M3.2 6h5.6M6 3.2v5.6" stroke="#7ab33d" stroke-width=".6"/></svg>
          www.talkwell.example
        </li>
      </ul>
    </aside>

    <div class="sign-off">
      <div class="signature" role="img" aria-label="Handwritten signature"></div>
      <div class="closing">Yours Sincerely,</div>
      <div class="signatory">Jordan Hale</div>
    </div>

    <div class="corner-mark"></div>

    <footer class="address">
      <div class="rule rule-green"></div>
      <div>Suite 4, 20 - 24 Harbour Lane<br>Brightwood VIC 3999</div>
      <div class="reg">Registered No: 000 123 45</div>
    </footer>
  </main>
</body>
</html>
```